THE TALL COPPER ATLAS OF PORTS

subtitle: AN INTRO TO SEARCH ENGINE OPTIMIZATION
background: white
dimensions: 1562x2500

Target Market(s)

Marketing professionals

Industry/Entity Type

Digital Marketing

Font styles to use
Sans Serif

Colors
ffffff
1b1b1b
3176b5

Requirements
Should not have
• Images or graphics

```html
<!DOCTYPE html>
<html lang="en">
<head>
<meta charset="UTF-8">
<title>The Tall Copper Atlas of Ports – Cover</title>
<link href="https://fonts.googleapis.com/css2?family=Raleway:wght@300;500;700&display=swap" rel="stylesheet">
<style>
  :root {
    --paper: #ffffff;
    --ink: #1b1b1b;
    --ink-soft: #4a4a4a;
    --accent: #3176b5;
    --stage: #ececec;
  }
  * { margin: 0; padding: 0; box-sizing: border-box; }
  html, body {
    width: 1200px;
    height: 800px;
    overflow: hidden;
    background: var(--stage);
  }
  .canvas {
    width: 1200px;
    height: 800px;
    display: flex;
    align-items: center;
    justify-content: center;
  }
  .cover {
    position: relative;
    width: 500px;
    height: 800px;
    background: var(--paper);
    font-family: "Raleway", sans-serif;
    color: var(--ink);
  }
  .cover__title {
    position: absolute;
    left: 120px;
    top: 150px;
    font-weight: 300;
    line-height: 1;
  }
  .cover__title-line {
    display: block;
    color: var(--accent);
    font-size: 62px;
    letter-spacing: 0.5px;
    margin-bottom: 6px;
  }
  .cover__title-line--indent { padding-left: 34px; }
  .cover__title-line--indent2 { padding-left: 16px; }
  .cover__title-key {
    display: block;
    color: var(--ink-soft);
    font-weight: 500;
    font-size: 120px;
    letter-spacing: -2px;
    margin-top: 4px;
    margin-left: -8px;
  }
  .cover__subtitle {
    position: absolute;
    left: 0;
    right: 0;
    top: 560px;
    text-align: center;
    padding-left: 60px;
    font-size: 13px;
    font-weight: 500;
    letter-spacing: 0.6px;
    line-height: 1.35;
    color: var(--ink);
  }
  .cover__author {
    position: absolute;
    left: 0;
    right: 0;
    top: 680px;
    text-align: center;
    padding-left: 60px;
    font-size: 22px;
    font-weight: 700;
    letter-spacing: 2.5px;
    color: var(--accent);
  }
</style>
</head>
<body>
  <main class="canvas">
    <section class="cover">
      <h1 class="cover__title">
        <span class="cover__title-line">The Tall</span>
        <span class="cover__title-line cover__title-line--indent">Copper</span>
        <span class="cover__title-line cover__title-line--indent2">Atlas of</span>
        <span class="cover__title-key">PORTS</span>
      </h1>
      <p class="cover__subtitle">AN INTRODUCTION TO SEARCH<br>ENGINE OPTIMIZATION</p>
      <p class="cover__author">LENNART OSTBY</p>
    </section>
  </main>
</body>
</html>
```